Business Cards that are elegant and wow

I want to create and print business cards that represent my brand and stand out from the rest. We want to ensure they stay in our branding and the integrity is not lost. I am happy to look at different shapes like square etc.

It will be printed on very thick cards and will be stylish .

I want to create and print business cards that represent my brand and stand out from the rest. We want to ensure they stay in ur branding and the integrity is not lost. I am happy to look at different shapes like square etc.

Target Market(s)

real estate professionals

Industry/Entity Type

Real Estate

Contact Information for Business Card

Maren Holt
hello@brightfernrealty.com.au
brightfernrealty.com.au
0487 316 252 (SMS)

Colors

Designer to choose colors to be used in the design.

Requirements
Must have
• My logo
• email
• website
• Name
Nice to have
• I like the idea of printing with foil or spot gloss. You want it to stand out in a sea.
Should not have
• I would like you to stay in my colour themes. Don't change the colour of my logo

```html
<!DOCTYPE html>
<html lang="en">
<head>
<meta charset="utf-8">
<title>Bright Fern Realty — Business Card</title>
<link rel="stylesheet" href="https://fonts.googleapis.com/css2?family=Montserrat:wght@400;500;700&display=swap">
<style>
  :root {
    --bg: #2a2b2e;
    --card-white: #ffffff;
    --brand-pink: #e8137a;
    --brand-pink-deep: #d60f6e;
    --brand-pink-light: #f2358f;
    --brand-blue: #26aae1;
    --card-shadow: rgba(0,0,0,0.45);
  }
  * { box-sizing: border-box; margin: 0; padding: 0; }
  html, body { width: 1200px; height: 960px; overflow: hidden; }
  body {
    background: var(--bg);
    font-family: "Montserrat", Arial, sans-serif;
    position: relative;
  }
  .card {
    position: absolute;
    width: 560px;
    height: 320px;
    border-radius: 28px;
    box-shadow: 0 18px 40px var(--card-shadow);
    overflow: hidden;
  }

  /* Back of card */
  .card-back {
    left: 580px;
    top: 110px;
    background: linear-gradient(135deg, var(--brand-pink-light) 0%, var(--brand-pink) 55%, var(--brand-pink-deep) 100%);
    display: flex;
    align-items: center;
    justify-content: center;
  }
  .card-back .pattern-field {
    position: absolute;
    inset: 0;
    background: linear-gradient(160deg, rgba(255,255,255,0.08) 0%, rgba(255,255,255,0) 60%, rgba(255,255,255,0.05) 100%);
  }
  .back-lockup {
    position: relative;
    display: flex;
    align-items: center;
    gap: 18px;
    color: var(--card-white);
  }
  .back-lockup .mark {
    width: 62px; height: 62px;
    border: 4px solid var(--card-white);
    border-radius: 50%;
  }
  .back-lockup .brand-name {
    font-weight: 700;
    font-size: 30px;
    letter-spacing: 2px;
    text-transform: uppercase;
  }

  /* Front of card */
  .card-front {
    left: 60px;
    top: 530px;
    background: var(--card-white);
    display: flex;
    align-items: center;
    padding: 0 36px 0 34px;
  }
  .front-brand {
    width: 200px;
    display: flex;
    flex-direction: column;
    align-items: center;
    gap: 14px;
  }
  .front-brand .mark {
    width: 130px; height: 130px;
    border: 9px solid var(--brand-blue);
    border-radius: 50%;
  }
  .front-brand .brand-name {
    color: var(--brand-pink);
    font-weight: 700;
    font-size: 15px;
    letter-spacing: 1.5px;
    text-transform: uppercase;
    text-align: center;
  }
  .divider {
    width: 4px;
    height: 230px;
    background: var(--brand-pink);
    margin: 0 26px 0 22px;
  }
  .contact { display: flex; flex-direction: column; }
  .contact .person-name {
    color: var(--brand-pink);
    font-weight: 700;
    font-size: 34px;
    text-transform: uppercase;
    letter-spacing: 1px;
    line-height: 1;
  }
  .contact .person-title {
    color: var(--brand-blue);
    font-weight: 500;
    font-size: 16px;
    text-transform: uppercase;
    margin: 6px 0 14px;
  }
  .contact-list { list-style: none; }
  .contact-list li {
    display: flex;
    align-items: flex-start;
    gap: 9px;
    color: var(--brand-blue);
    font-size: 15px;
    line-height: 1.45;
  }
  .contact-list svg { width: 14px; height: 14px; margin-top: 4px; flex: none; fill: var(--brand-pink); }
</style>
</head>
<body>

  <section class="card card-back" aria-label="Card back">
    <div class="pattern-field" role="img" aria-label="Faint repeated brand name pattern across the pink field"></div>
    <div class="back-lockup">
      <span class="mark"></span>
      <span class="brand-name">Bright Fern Realty</span>
    </div>
  </section>

  <section class="card card-front" aria-label="Card front">
    <div class="front-brand">
      <span class="mark"></span>
      <span class="brand-name">Bright Fern Realty</span>
    </div>
    <span class="divider"></span>
    <div class="contact">
      <h1 class="person-name">Maren Holt</h1>
      <p class="person-title">Your Title</p>
      <ul class="contact-list">
        <li>
          <svg viewBox="0 0 24 24"><path d="M6.6 10.8a15 15 0 0 0 6.6 6.6l2.2-2.2c.3-.3.7-.4 1-.2 1.1.4 2.3.6 3.6.6.6 0 1 .4 1 1V20c0 .6-.4 1-1 1A17 17 0 0 1 3 4c0-.6.4-1 1-1h3.5c.6 0 1 .4 1 1 0 1.3.2 2.5.6 3.6.1.3 0 .7-.2 1z"/></svg>
          0487 316 252
        </li>
        <li>
          <svg viewBox="0 0 24 24"><path d="M2 5h20v14H2zm2 2v.5l8 5 8-5V7zm0 2.9V17h16V9.9l-8 5z"/></svg>
          hello@brightfernrealty.com.au
        </li>
        <li>
          <svg viewBox="0 0 24 24"><path d="M12 2a10 10 0 1 0 0 20 10 10 0 0 0 0-20zm6.9 9h-3a15 15 0 0 0-1.3-5.6A8 8 0 0 1 18.9 11zM12 4.1c.9 1.3 1.8 3.6 1.9 6.9h-3.8c.1-3.3 1-5.6 1.9-6.9zM9.4 5.4A15 15 0 0 0 8.1 11h-3a8 8 0 0 1 4.3-5.6zM5.1 13h3a15 15 0 0 0 1.3 5.6A8 8 0 0 1 5.1 13zm6.9 6.9c-.9-1.3-1.8-3.6-1.9-6.9h3.8c-.1 3.3-1 5.6-1.9 6.9zm2.6-1.3a15 15 0 0 0 1.3-5.6h3a8 8 0 0 1-4.3 5.6z"/></svg>
          brightfernrealty.com.au
        </li>
        <li>
          <svg viewBox="0 0 24 24"><path d="M12 2a7 7 0 0 0-7 7c0 5 7 13 7 13s7-8 7-13a7 7 0 0 0-7-7zm0 9.5A2.5 2.5 0 1 1 12 6.5a2.5 2.5 0 0 1 0 5z"/></svg>
          <span>Your address, city<br>state, ZIP 0000</span>
        </li>
      </ul>
    </div>
  </section>

</body>
</html>
```